Business Card Design

I need a good card to sell my talents in the music field and get my name known as a musician/Guitarist

Industry/Entity Type

Business

Contact Information for Business Card

Nathaniel Brisco Musician/Guitarist

```html
<!DOCTYPE html>
<html lang="en">
<head>
<meta charset="utf-8">
<title>Nathaniel Brisco – Business Card</title>
<link rel="stylesheet" href="https://fonts.googleapis.com/css2?family=Marcellus&display=swap">
<style>
  :root {
    --stage: #efe6dc;
    --red-deep: #b5000a;
    --red-mid: #d6101a;
    --red-bright: #f21c24;
    --ink-light: #ffffff;
    --ink-red: #a3141c;
    --sky: #9fe8fb;
    --mist: #f4f8fb;
    --lilac: #d9d6fb;
    --note-orange: #f07a2a;
    --note-red: #d5121d;
  }
  html, body {
    margin: 0;
    width: 1200px;
    height: 697px;
    overflow: hidden;
    background: var(--stage);
  }
  .stage {
    position: relative;
    width: 1200px;
    height: 697px;
    font-family: "Marcellus", serif;
  }
  .card {
    position: absolute;
    top: 110px;
    width: 330px;
    height: 480px;
    border-radius: 20px;
    overflow: hidden;
    box-shadow: 0 10px 24px rgba(80, 40, 10, 0.25);
  }
  /* Front */
  .card-front {
    left: 230px;
    background: linear-gradient(125deg, var(--red-deep) 0%, var(--red-bright) 22%, var(--red-mid) 45%, var(--red-deep) 62%, var(--red-bright) 80%, var(--red-deep) 100%);
    color: var(--ink-light);
    text-align: center;
  }
  .front-motif {
    position: absolute;
    left: 90px;
    top: 92px;
    width: 150px;
    height: 95px;
    border-radius: 6px;
    background: linear-gradient(180deg, rgba(255,255,255,0.85), rgba(255,255,255,0.6));
  }
  .rule {
    position: absolute;
    left: 36px;
    right: 36px;
    height: 2px;
    background: var(--ink-light);
  }
  .rule-top { top: 222px; }
  .rule-bottom { top: 278px; }
  .holder-name {
    position: absolute;
    top: 232px;
    left: 0;
    right: 0;
    font-size: 21px;
    letter-spacing: 0.3px;
  }
  .holder-role {
    position: absolute;
    top: 258px;
    left: 0;
    right: 0;
    font-size: 12px;
  }
  .address {
    position: absolute;
    top: 302px;
    left: 0;
    right: 0;
    font-size: 14px;
    line-height: 19px;
  }
  .contact {
    position: absolute;
    left: 0;
    right: 0;
    display: flex;
    justify-content: center;
    align-items: center;
    gap: 7px;
    font-size: 14px;
  }
  .contact svg { width: 13px; height: 13px; }
  .contact-phone { top: 372px; }
  .contact-web { top: 404px; }
  /* Back */
  .card-back {
    left: 640px;
    background: linear-gradient(160deg, var(--sky) 0%, var(--mist) 38%, #ffffff 55%, var(--lilac) 85%, var(--mist) 100%);
    text-align: center;
  }
  .back-motif {
    position: absolute;
    left: 65px;
    top: 160px;
    width: 200px;
    height: 120px;
    border-radius: 6px;
    background: linear-gradient(135deg, var(--note-orange), var(--note-red));
  }
  .back-role {
    position: absolute;
    top: 298px;
    left: 0;
    right: 0;
    font-size: 19px;
    color: var(--ink-red);
  }
</style>
</head>
<body>
<main class="stage">
  <section class="card card-front">
    <div class="front-motif" role="img" aria-label="White music staff with treble clef and notes"></div>
    <div class="rule rule-top"></div>
    <div class="holder-name">Nathaniel Brisco</div>
    <div class="holder-role">Musician | Guitaris</div>
    <div class="rule rule-bottom"></div>
    <div class="address">218 Quarry Lane, Elm Crossing<br>New York 10990</div>
    <div class="contact contact-phone">
      <svg viewBox="0 0 24 24" aria-hidden="true"><path fill="#fff" d="M6.6 10.8a15.1 15.1 0 0 0 6.6 6.6l2.2-2.2c.3-.3.7-.4 1-.2 1.1.4 2.3.6 3.6.6.6 0 1 .4 1 1V20c0 .6-.4 1-1 1A17 17 0 0 1 3 4c0-.6.4-1 1-1h3.5c.6 0 1 .4 1 1 0 1.3.2 2.5.6 3.6.1.3 0 .7-.2 1z"/></svg>
      <span>555-201-4830</span>
    </div>
    <div class="contact contact-web">
      <svg viewBox="0 0 24 24" aria-hidden="true" fill="none" stroke="#fff" stroke-width="1.8"><circle cx="12" cy="12" r="10"/><ellipse cx="12" cy="12" rx="4.5" ry="10"/><path d="M2 12h20M4 7h16M4 17h16"/></svg>
      <span>nathanielbrisco.com</span>
    </div>
  </section>

  <section class="card card-back">
    <div class="back-motif" role="img" aria-label="Orange and red music staff with treble clef and notes"></div>
    <div class="back-role">Musician | Guitaris</div>
  </section>
</main>
</body>
</html>
```